7:35 Harbor Compass Method- A Handbook So Your Crew Trusts Each Step You Take

7:35 Harbor Compass Method
A Handbook So Your Crew Trusts Each Step You Take

It will be a 6 X 9 guide that is meant for people to keep with them with pages to fill out. See supporting pics for overall pillars that are discussed and form basis of the solution.

I will need a spine and back cover as well.

My blog and content: www.morvenqtallis.example

Target Market(s)

Business professionals, senior emergency services people

Industry/Entity Type

Business Management

Font styles to use
Serif

Colors

Designer to choose colors to be used in the design.

Requirements
Must have
• Clean look, easily recognizable among other books. Front cover and back and spine. My picture on the back somewhere (corner maybe?!)
Nice to have
• Easily recognizeable
• NOTE: Graphic should read Today, Was I the Leader That I Would Want? I uploaded graphic that says ..."I Would've Wanted" which is incorrect.
Should not have
• Busy cover

```html
<!DOCTYPE html>
<html lang="en">
<head>
<meta charset="utf-8">
<title>7:35 Harbor Compass Method – Book Cover</title>
<link href="https://fonts.googleapis.com/css2?family=Oswald:wght@400;500;600&family=Arimo:wght@400&display=swap" rel="stylesheet">
<style>
  :root {
    --stage: #000000;
    --paper: #f4f4f4;
    --paper-shade: #e6e6e8;
    --red: #c4161c;
    --ink: #1c1c1c;
    --grey-ink: #3a3a3a;
    --rule: #2a2a2a;
    --portrait: #050505;
  }
  * { margin: 0; padding: 0; box-sizing: border-box; }
  html, body { width: 1200px; height: 1200px; overflow: hidden; background: var(--stage); }
  .canvas { position: relative; width: 1200px; height: 1200px; background: var(--stage); }

  .book-wrap {
    position: absolute; left: 60px; top: 237px; width: 1080px; height: 731px;
    background: var(--paper); overflow: hidden;
  }

  /* Back cover */
  .back-cover { position: absolute; left: 0; top: 0; width: 510px; height: 731px; }
  .back-title {
    position: absolute; left: 37px; top: 24px;
    font-family: "Oswald", sans-serif; font-weight: 500; font-size: 33px;
    color: var(--red); letter-spacing: 0.5px; white-space: nowrap;
  }
  .back-copy {
    position: absolute; left: 37px; top: 76px; width: 435px;
    font-family: "Arimo", Arial, sans-serif; font-size: 13.2px; line-height: 16px;
    color: var(--ink); text-align: justify;
  }
  .back-copy p + p { margin-top: 16px; }
  .back-rule { position: absolute; left: 37px; top: 438px; width: 435px; height: 1px; background: var(--rule); }
  .author-portrait {
    position: absolute; left: 37px; top: 460px; width: 101px; height: 140px; background: var(--portrait);
  }
  .author-bio {
    position: absolute; left: 157px; top: 460px; width: 315px;
    font-family: "Arimo", Arial, sans-serif; font-size: 13.2px; line-height: 16px;
    color: var(--ink); text-align: justify;
  }
  .back-website {
    position: absolute; left: 37px; top: 694px;
    font-family: "Arimo", Arial, sans-serif; font-size: 13px; color: var(--ink);
  }
  .back-fade {
    position: absolute; left: 0; bottom: 0; width: 510px; height: 300px;
    background: linear-gradient(to bottom, rgba(230,230,232,0), var(--paper-shade));
  }

  /* Spine */
  .spine { position: absolute; left: 510px; top: 0; width: 75px; height: 731px; }
  .spine-title, .spine-author {
    position: absolute; left: 50%; white-space: nowrap;
    transform-origin: center; font-family: "Oswald", sans-serif;
  }
  .spine-title {
    top: 255px; transform: translate(-50%, -50%) rotate(90deg);
    font-weight: 500; font-size: 34px; color: var(--red); letter-spacing: 0.5px;
  }
  .spine-author {
    top: 600px; transform: translate(-50%, -50%) rotate(90deg);
    font-weight: 400; font-size: 22px; color: var(--ink);
  }

  /* Front cover */
  .front-cover { position: absolute; left: 585px; top: 0; width: 495px; height: 731px; }
  .front-scene {
    position: absolute; left: 0; top: 330px; width: 495px; height: 401px;
    background: linear-gradient(to bottom, var(--paper) 0%, var(--paper-shade) 100%);
  }
  .front-title {
    position: absolute; left: 0; top: 18px; width: 495px; text-align: center;
    font-family: "Oswald", sans-serif; font-weight: 500; color: var(--red);
    font-size: 74px; line-height: 75px; letter-spacing: 1px;
  }
  .front-subtitle {
    position: absolute; left: 30px; top: 332px; width: 440px; text-align: center;
    border-top: 1.5px solid var(--rule); border-bottom: 1.5px solid var(--rule);
    padding: 8px 0 7px;
    font-family: "Oswald", sans-serif; font-weight: 400; font-size: 19px; line-height: 22px;
    color: var(--ink); text-transform: uppercase;
  }
  .front-author {
    position: absolute; left: 0; top: 650px; width: 495px; text-align: center;
    font-family: "Oswald", sans-serif; font-weight: 400; font-size: 31px; color: var(--grey-ink);
    letter-spacing: 0.5px;
  }
</style>
</head>
<body>
<div class="canvas">
  <div class="book-wrap">

    <section class="back-cover">
      <div class="back-fade" role="img" aria-label="Faint field of white paper boats fading into the background"></div>
      <h2 class="back-title">7:35 HARBOR COMPASS METHOD</h2>
      <div class="back-copy">
        <p>Lorem ipsum dolor sit amet, consectetur adipiscing elit, sed do eiusmod tempor incididunt ut labore et dolore magna aliqua. Ut enim ad minim veniam, quis nostrud exercitation ullamco laboris nisi ut aliquip ex ea commodo consequat. Duis aute irure dolor in reprehenderit in voluptate velit esse cillum dolore eu fugiat nulla pariatur. Excepteur sint occaecat cupidatat non proident, sunt in culpa qui officia deserunt mollit anim id est laborum.</p>
        <p>Sed ut perspiciatis unde omnis iste natus error sit voluptatem accusantium doloremque laudantium, totam rem aperiam, eaque ipsa quae ab illo inventore veritatis et quasi architecto beatae vitae dicta sunt explicabo. Nemo enim ipsam voluptatem quia voluptas sit aspernatur aut odit aut fugit, sed quia consequuntur magni dolores eos qui ratione voluptatem sequi nesciunt. Neque porro quisquam est, qui dolorem ipsum quia dolor sit amet, consectetur, adipisci velit, sed quia non numquam eius modi tempora incidunt ut labore et dolore magnam aliquam quaerat voluptatem. Ut enim ad minima veniam, quis nostrum exercitationem ullam corporis suscipit laboriosam, nisi ut aliquid ex ea commodi consequatur? Quis autem vel eum iure reprehenderit qui in ea voluptate velit esse quam nihil molestiae consequatur, vel illum qui dolorem eum fugiat quo voluptas nulla pariatur?</p>
      </div>
      <div class="back-rule"></div>
      <div class="author-portrait" role="img" aria-label="Author portrait"></div>
      <p class="author-bio">Lorem ipsum dolor sit amet, consectetur adipiscing elit, sed do eiusmod tempor incididunt ut labore et dolore magna aliqua. Ut enim ad minim veniam, quis nostrud exercitation ullamco laboris nisi ut aliquip ex ea commodo consequat. Duis aute irure dolor in reprehenderit in voluptate velit esse cillum dolore eu fugiat nulla pariatur. Excepteur sint occaecat cupidatat non proident, sunt in culpa qui officia deserunt mollit anim id est laborum.</p>
      <p class="back-website">www.morvenqtallis.example</p>
    </section>

    <section class="spine">
      <div class="spine-title">7:35 HARBOR COMPASS METHOD</div>
      <div class="spine-author">MORVEN Q. TALLIS</div>
    </section>

    <section class="front-cover">
      <div class="front-scene" role="img" aria-label="White paper boats in a grid with one red paper boat breaking away along a dotted path"></div>
      <h1 class="front-title">7:35<br>HARBOR<br>COMPASS<br>METHOD</h1>
      <p class="front-subtitle">A Handbook So Your Crew Trusts<br>Each Step You Take</p>
      <p class="front-author">MORVEN Q. TALLIS</p>
    </section>

  </div>
</div>
</body>
</html>
```